CoverBeacon Gap Insurance InfoGraphic

We need an infographic detailing what Gap insurance is, the types, and who needs it. All of this information can be found in the attached report. Please adhere to the same branding style as our website, www.coverbeacon-example.com

Target Market(s)

people age 64+ and their families

Industry/Entity Type

Insurance

Requirements
Must have
• Must cover multiple facets of gap insurance, not just "what is it"

```html
<!DOCTYPE html>
<html lang="en">
<head>
<meta charset="utf-8">
<title>Medigap Insurance</title>
<link rel="stylesheet" href="https://fonts.googleapis.com/css2?family=Source+Sans+3:wght@300;400;600&display=swap">
<style>
  :root {
    --sky: #9ae4fa;
    --ink: #0b4a5c;
    --glass-edge: #e9fbff;
    --glass-fill: #a9e9fc;
    --badge-light: #fbac82;
    --badge-dark: #ef6b33;
    --cell-rim: #2f8fd0;
    --note-text: #24323a;
  }
  html, body {
    margin: 0;
    padding: 0;
    width: 1200px;
    height: 1179px;
    overflow: hidden;
    background: var(--sky);
  }
  .infographic {
    display: block;
    width: 1200px;
    height: 1179px;
    font-family: "Source Sans 3", "Myriad Pro", sans-serif;
  }
  .plan-title {
    fill: var(--ink);
    font-weight: 600;
    font-size: 44px;
    text-anchor: middle;
  }
  .plan-detail {
    fill: #1d3f4c;
    font-weight: 300;
    font-size: 11px;
    text-anchor: middle;
  }
  .hero-title {
    fill: #ffffff;
    font-weight: 600;
    font-size: 46px;
    text-anchor: middle;
  }
  .intro-note {
    fill: var(--note-text);
    font-weight: 300;
    font-size: 16.5px;
    text-anchor: middle;
  }
  .intro-frame {
    fill: none;
    stroke: #22313a;
    stroke-width: 1.2;
    stroke-dasharray: 2 2;
  }
  .glass-frame {
    fill: var(--glass-fill);
    fill-opacity: 0.45;
    stroke: var(--glass-edge);
    stroke-width: 3;
  }
  .glass-shade {
    fill: none;
    stroke: #2a3c44;
    stroke-width: 2;
    stroke-opacity: 0.55;
  }
</style>
</head>
<body>
<svg class="infographic" viewBox="0 0 1361 1337" xmlns="http://www.w3.org/2000/svg">
  <defs>
    <radialGradient id="cell-fill" cx="50%" cy="50%" r="55%">
      <stop offset="0" stop-color="#c4f1ff"/>
      <stop offset="0.6" stop-color="#aee6fb"/>
      <stop offset="0.78" stop-color="#6ab6e2"/>
      <stop offset="0.92" stop-color="#2b6fa6"/>
      <stop offset="1" stop-color="#1a4f80"/>
    </radialGradient>
    <linearGradient id="hero-fill" x1="0" y1="0" x2="1" y2="1">
      <stop offset="0" stop-color="var(--badge-light)"/>
      <stop offset="0.5" stop-color="#f27e4a"/>
      <stop offset="1" stop-color="var(--badge-dark)"/>
    </linearGradient>
    <g id="plan-cell">
      <polygon class="glass-frame" points="-155,0 -77,-135 77,-135 155,0 77,135 -77,135"/>
      <polyline class="glass-shade" points="-150,8 -77,131"/>
      <polyline class="glass-shade" points="82,-128 150,-10"/>
      <polygon points="-130,0 -65,-113 65,-113 130,0 65,113 -65,113" fill="url(#cell-fill)" stroke="var(--cell-rim)" stroke-width="2.5"/>
    </g>
  </defs>

  <rect width="1361" height="1337" fill="var(--sky)"/>

  <!-- Hero badge -->
  <g class="hero-badge" transform="translate(685,208)">
    <polygon class="glass-frame" points="-195,0 -97,-169 97,-169 195,0 97,169 -97,169"/>
    <polyline class="glass-shade" points="-188,10 -97,164"/>
    <polyline class="glass-shade" points="103,-160 188,-12"/>
    <polygon points="-162,0 -81,-139 81,-139 162,0 81,139 -81,139" fill="url(#hero-fill)"/>
    <text class="hero-title" x="5" y="-8">Medigap</text>
    <text class="hero-title" x="10" y="50">Insurance</text>
  </g>

  <!-- Intro note -->
  <rect class="intro-frame" x="395" y="383" width="575" height="114"/>
  <text class="intro-note" x="682" y="412">Medigap is unique because it is offered through private insurance providers.</text>
  <text class="intro-note" x="682" y="434">It is required that you pay a monthly premium for Medicare Part B.</text>
  <text class="intro-note" x="682" y="456">It is important to understand Medicare Supplement plans have costs and</text>
  <text class="intro-note" x="682" y="478">benefits that depend on which Medigap plan you select.</text>

  <!-- Left column pair -->
  <g class="plan plan-a" transform="translate(252,540)">
    <use href="#plan-cell"/>
    <text class="plan-title" y="-23">Plan A</text>
    <text class="plan-detail" y="11">Plan A is the basic</text>
    <text class="plan-detail" y="26">Medigap plan</text>
    <text class="plan-detail" y="40">with copayments.</text>
    <text class="plan-detail" y="55">Plan A covers 20% on</text>
    <text class="plan-detail" y="69">outpatient treatment.</text>
  </g>
  <g class="plan plan-b" transform="translate(520,683)">
    <use href="#plan-cell"/>
    <text class="plan-title" y="-28">Plan B</text>
    <text class="plan-detail" y="-11">Plan B offers the same</text>
    <text class="plan-detail" y="4">benefits as Plan A.</text>
    <text class="plan-detail" y="19">It also covers Medicare</text>
    <text class="plan-detail" y="33">Part A hospital deductible</text>
    <text class="plan-detail" y="48">and pays the deductible</text>
    <text class="plan-detail" y="63">several times in the</text>
    <text class="plan-detail" y="77">same year, if needed.</text>
  </g>
  <g class="plan plan-c" transform="translate(248,837)">
    <use href="#plan-cell"/>
    <text class="plan-title" y="8">Plan C</text>
  </g>
  <g class="plan plan-d" transform="translate(520,980)">
    <use href="#plan-cell"/>
    <text class="plan-title" y="18">Plan D</text>
  </g>
  <g class="plan plan-f" transform="translate(248,1137)">
    <use href="#plan-cell"/>
    <text class="plan-title" y="5">Plan F</text>
  </g>

  <!-- Right column pair -->
  <g class="plan plan-k" transform="translate(850,680)">
    <use href="#plan-cell"/>
    <text class="plan-title" y="0">Plan K</text>
  </g>
  <g class="plan plan-m" transform="translate(850,978)">
    <use href="#plan-cell"/>
    <text class="plan-title" y="5">Plan M</text>
  </g>
  <g class="plan plan-g" transform="translate(1122,518)">
    <use href="#plan-cell"/>
    <text class="plan-title" y="26">Plan G</text>
  </g>
  <g class="plan plan-l" transform="translate(1122,818)">
    <use href="#plan-cell"/>
    <text class="plan-title" y="24">Plan L</text>
  </g>
  <g class="plan plan-n" transform="translate(1122,1120)">
    <use href="#plan-cell"/>
    <text class="plan-title" y="14">Plan N</text>
  </g>
</svg>
</body>
</html>
```